Boutique custom software development company needs new business card

Our nearly 20 year old custom software development company would like to better include the fact that we are now providing plain circle decoration services. These new services are B2B include education (how to acquire and securely hold plain circle decoration) and integrating plain circle decoration payments into existing ecommerce sites or other existing systems. Please keep the card clean and simple. Attached is our current design and some other files. velquor.example

Target Market(s)

businesses owners interested in long term relationship

Industry/Entity Type

Custom software development and plain circle decoration

Contact Information for Business Card

Dale Furness, dale@velquor.example, velquor.example, (555) 274-VELQ

Font styles to use
Other font styles liked:
• monospace

Requirements
Must have
• double-sided
Nice to have
• clean and simple
Should not have
• physical address

```html
<!DOCTYPE html>
<html lang="en">
<head>
<meta charset="utf-8">
<title>Dale Furness — Business Card</title>
<link href="https://fonts.googleapis.com/css2?family=Open+Sans:wght@400;600;700;800&display=swap" rel="stylesheet">
<style>
  :root {
    --stage: #464648;
    --paper: #ffffff;
    --brand-blue: #3b74bb;
    --brand-orange: #f07d22;
    --ink: #3a3a3a;
  }
  * { margin: 0; padding: 0; box-sizing: border-box; }
  html, body {
    width: 1200px;
    height: 770px;
    overflow: hidden;
    background: var(--stage);
  }
  .stage {
    position: relative;
    width: 1200px;
    height: 770px;
    display: flex;
    justify-content: center;
    align-items: center;
    gap: 60px;
  }
  .card {
    position: relative;
    width: 340px;
    height: 612px;
    background: var(--paper);
    overflow: hidden;
    box-shadow: 0 10px 18px rgba(0, 0, 0, 0.45);
    font-family: "Open Sans", sans-serif;
  }

  /* Front side */
  .holder-name {
    position: absolute;
    left: 156px;
    top: 40px;
    transform-origin: top left;
    transform: rotate(90deg);
    color: var(--brand-orange);
    font-weight: 800;
    font-size: 58px;
    line-height: 0.98;
    text-transform: uppercase;
    white-space: nowrap;
    letter-spacing: -0.5px;
  }
  .holder-name span { display: block; }
  .contact-phone {
    position: absolute;
    left: 49px;
    top: 312px;
    color: var(--brand-blue);
    font-weight: 700;
    font-size: 31px;
    letter-spacing: -0.3px;
  }
  .contact-email {
    position: absolute;
    left: 49px;
    top: 357px;
    color: var(--ink);
    font-weight: 400;
    font-size: 18px;
  }
  .front-ring {
    position: absolute;
    left: -60px;
    top: 420px;
    width: 320px;
    height: 320px;
  }

  /* Back side */
  .brand-square {
    position: absolute;
    left: 43px;
    top: 43px;
    width: 254px;
    height: 254px;
    background: var(--brand-blue);
  }
  .brand-block {
    position: absolute;
    left: 0;
    right: 0;
    top: 440px;
    text-align: center;
  }
  .brand-name {
    color: var(--brand-blue);
    font-weight: 800;
    font-size: 50px;
    line-height: 1;
    letter-spacing: 0.5px;
  }
  .brand-tagline {
    margin-top: 8px;
    color: var(--brand-blue);
    font-weight: 400;
    font-size: 18px;
    letter-spacing: -0.6px;
  }
  .brand-web {
    margin-top: 12px;
    color: var(--ink);
    font-weight: 400;
    font-size: 16px;
    letter-spacing: 1.5px;
  }
</style>
</head>
<body>
  <main class="stage">
    <section class="card card-front" aria-label="Card front">
      <h1 class="holder-name"><span>Dale</span><span>Furness</span></h1>
      <p class="contact-phone">555.274.0199</p>
      <p class="contact-email">dale@velquor.example</p>
      <svg class="front-ring" viewBox="0 0 320 320" aria-hidden="true">
        <circle cx="160" cy="160" r="150" fill="none" stroke="var(--brand-orange)" stroke-width="2.5"/>
      </svg>
    </section>

    <section class="card card-back" aria-label="Card back">
      <div class="brand-square"></div>
      <div class="brand-block">
        <p class="brand-name">VELQUOR</p>
        <p class="brand-tagline">developer of custom applications</p>
        <p class="brand-web">velquor.example</p>
      </div>
    </section>
  </main>
</body>
</html>
```